Fun/Happy Business Card & New Logo for Home Cake Shop

We need a business card for a small home-based, 2 person husband/wife bakery where we do cakes, cupcakes, eclairs, cream puffs and such. Our company name is Plum Crumb Bakehouse.

We generally like the colour pink, but are open to other colour scheme ideas as well. The head chef(wife) is a very fun-loving, always cheerful and happy person and we want the business card to reflect her bubbly personality.

The business card should contain the husband's name AND the wife's name.
Updates

1st place prize money has been increased as requested. Thanks for your designs so far! 

Target Market(s)

Generally adults, for birthdays or small/medium sized catering events.

Industry/Entity Type

Bakery

Requirements
Must have
• Name 1: Soraya Pettit
Phone: 93816275

Name 2: Marcel Pettit
Phone: 96214853

Email: info@plumcrumbbakehouse.com
Website: www.plumcrumbbakehouse.com

Additional Info, Edit: Please ensure that the logo contains a cake and at least a couple cupcakes.
Nice to have
• I have uploaded a couple images with the general feel of what we want. The logo should be one with a cake and some cupcakes around it, with the words Plum Crumb Bakehouse. Try to come up with something more impressive than the current logo we have.

For the draft name card I uploaded in the file, that is also what we're sort of looking at. Try to come up with something more impressive/creative than that name card as well.

For the back of the name card, we are happy with just having the logo there. We're not sure what colour scheme would go best just yet, so feel free to show us your creative minds! :)

Additional Info, Edit: Please try to come up with a more realistic type of cake and cupcakes in the logo. We do not want it to be too cartoony. The attached images are just examples of the format.
Should not have
• Wordings or images that indicate 'Phone', 'Email' or 'Website' do not need to be included. Our customer base should be able to identify what an email and a website looks like. However, if you find that it looks particularly better, then feel free to be creative.

```html
<!DOCTYPE html>
<html lang="en">
<head>
<meta charset="utf-8">
<title>Plum Crumb Bakehouse – Business Card</title>
<link href="https://fonts.googleapis.com/css2?family=Marcellus&display=swap" rel="stylesheet">
<style>
  :root {
    --page: #ffffff;
    --plum: #c475a7;
    --cream: #f2f1ef;
    --card-text: #f4eef2;
  }
  html, body {
    margin: 0;
    padding: 0;
    width: 1100px;
    height: 1200px;
    overflow: hidden;
    background: var(--page);
  }
  .canvas {
    position: relative;
    width: 1100px;
    height: 1200px;
  }
  .card {
    position: absolute;
    left: 124px;
    width: 850px;
  }
  .card--front {
    top: 84px;
    height: 499px;
    background: var(--cream);
  }
  .card--back {
    top: 615px;
    height: 499px;
    background: var(--plum);
  }
  .brand-badge {
    position: absolute;
    left: 224px;
    top: 59px;
    width: 380px;
    height: 380px;
    border-radius: 50%;
    background: var(--plum);
    display: flex;
    align-items: center;
    justify-content: center;
  }
  .brand-name {
    margin: 0;
    font-family: "Marcellus", serif;
    font-weight: 400;
    font-size: 62px;
    line-height: 0.98;
    letter-spacing: 1px;
    color: var(--cream);
    text-align: center;
  }
  .brand-name__line {
    display: block;
  }
  .contact {
    position: absolute;
    left: 178px;
    top: 176px;
    font-family: "Marcellus", serif;
    font-size: 29px;
    line-height: 45px;
    color: var(--card-text);
    letter-spacing: 0.6px;
    white-space: nowrap;
  }
  .contact__person {
    display: grid;
    grid-template-columns: 230px auto;
  }
  .contact__row {
    display: block;
  }
</style>
</head>
<body>
  <main class="canvas">
    <section class="card card--front">
      <div class="brand-badge">
        <h1 class="brand-name">
          <span class="brand-name__line">Plum</span>
          <span class="brand-name__line">Crumb</span>
          <span class="brand-name__line">Bakehouse</span>
        </h1>
      </div>
    </section>

    <section class="card card--back">
      <div class="contact">
        <div class="contact__person">
          <span class="contact__name">Marcel Pettit</span>
          <span class="contact__phone">phone: 96214853</span>
        </div>
        <div class="contact__person">
          <span class="contact__name">Soraya Pettit</span>
          <span class="contact__phone">phone: 93816275</span>
        </div>
        <div class="contact__row">email: info@plumcrumbbakehouse.com</div>
        <div class="contact__row">website: www.plumcrumbbakehouse.com</div>
      </div>
    </section>
  </main>
</body>
</html>
```